Tile Installation business needs a van wrap design using supplied logo

Need wrap designed for a 2023 Dalvor Kestrix Mover cargo van with the supplied logos. Looking at all options lettering kits, half wraps, and full wrap designs. We install floor tiles and build new showers, and backsplashes. The final design should catch the eye of someone when driving on the road and not be too cluttered.

```html
<!DOCTYPE html>
<html lang="en">
<head>
<meta charset="utf-8">
<title>Meridell Tile &amp; Stone — Van Wrap Side Panel</title>
<link rel="stylesheet" href="https://fonts.googleapis.com/css2?family=Montserrat:wght@500;600;700&display=swap">
<style>
  :root {
    --stage: #ececec;
    --wrap-white: #ffffff;
    --brand-green: #2e9a4e;
    --brand-green-light: #8fd14f;
    --ink: #111111;
    --text-dark: #2a2a2a;
    --text-light: #ffffff;
  }
  html, body {
    margin: 0;
    padding: 0;
    width: 1200px;
    height: 720px;
    overflow: hidden;
    background: var(--stage);
  }
  .canvas {
    position: relative;
    width: 1200px;
    height: 720px;
  }
  .wrap-panel {
    position: absolute;
    left: 50px;
    top: 140px;
    width: 1100px;
    height: 440px;
    box-shadow: 0 14px 30px rgba(0,0,0,0.12);
  }
  .wrap-panel text {
    font-family: "Montserrat", sans-serif;
  }
  .panel-base { fill: var(--wrap-white); }
  .green-field { fill: var(--brand-green); }
  .black-field { fill: var(--ink); }
  .rocker-band { fill: var(--ink); }
  .service-bullet { fill: var(--brand-green-light); }
  .service-item {
    fill: var(--text-light);
    font-size: 26px;
    font-weight: 600;
  }
  .website {
    fill: var(--text-dark);
    font-size: 22px;
    font-weight: 500;
    letter-spacing: 0.5px;
  }
  .phone {
    fill: var(--text-light);
    font-size: 46px;
    font-weight: 700;
  }
  .brand-name {
    fill: var(--text-dark);
    font-size: 34px;
    font-weight: 500;
  }
  .brand-square { fill: var(--brand-green); }
</style>
</head>
<body>
<main class="canvas">
  <svg class="wrap-panel" viewBox="0 0 1100 440" width="1100" height="440" aria-label="Van wrap side panel for Meridell Tile &amp; Stone">
    <rect class="panel-base" x="0" y="0" width="1100" height="440"/>

    <!-- upper service field -->
    <polygon class="green-field" points="360,0 1100,0 1100,205 460,205"/>
    <!-- diagonal stripe -->
    <polygon class="green-field" points="460,205 565,205 790,440 680,440"/>

    <!-- lower contact field -->
    <path class="black-field" d="M730,250 H1100 V440 H810 L700,300 Q690,262 730,250 Z"/>

    <!-- rocker band -->
    <polygon class="rocker-band" points="140,390 700,375 720,410 150,420"/>

    <!-- services -->
    <g class="services">
      <rect class="service-bullet" x="490" y="70" width="9" height="9"/>
      <text class="service-item" x="508" y="84">Tile Installation</text>
      <rect class="service-bullet" x="490" y="118" width="9" height="9"/>
      <text class="service-item" x="508" y="132">Kitchens</text>
      <rect class="service-bullet" x="780" y="70" width="9" height="9"/>
      <text class="service-item" x="796" y="84">Bathrooms</text>
      <rect class="service-bullet" x="780" y="118" width="9" height="9"/>
      <text class="service-item" x="796" y="132">Floors &amp; More</text>
    </g>

    <text class="website" x="1075" y="236" text-anchor="end">www.meridelltileandstone.com</text>
    <text class="phone" x="1075" y="316" text-anchor="end">555-214-0387</text>

    <!-- brand name -->
    <g class="brand">
      <rect class="brand-square" x="90" y="304" width="26" height="26"/>
      <text class="brand-name" x="128" y="329">Meridell Tile &amp; Stone</text>
    </g>
  </svg>
</main>
</body>
</html>
```